Label design for Japanese healthy drink

We need new label design to give our product a new look. This is Amazake, traditional Japanese drink made out of fermented rice. This is nutrition packed drink and target audience is health conscious people. We want something simple and healthy. The attached photo is current label (for the size reference only) and food pouch the label will be attached. Please don't use anything on the label in the picture.

Target Market(s)

health conscious people (30s - 50s)

Requirements
Must have
• "Amazake"
Should not have
• too much color, picture of rice or sake

```html
<!DOCTYPE html>
<html lang="en">
<head>
<meta charset="utf-8">
<title>Amazake Label</title>
<link rel="stylesheet" href="https://fonts.googleapis.com/css2?family=Montserrat:wght@400&family=Noto+Serif+JP:wght@400&family=Dela+Gothic+One&display=swap">
<style>
  :root {
    --page: #ffffff;
    --lime: #dfe84a;
    --lime-soft: #e6ec6e;
    --cream: #ebe3cf;
    --pink-line: #f09ac6;
    --magenta: #e3178e;
    --ink: #111111;
    --grey: #3a3a3a;
  }
  html, body {
    margin: 0;
    width: 1200px;
    height: 1200px;
    overflow: hidden;
    background: var(--page);
  }
  .canvas {
    position: relative;
    width: 1200px;
    height: 1200px;
  }
  .label {
    position: absolute;
    left: 100px;
    top: 120px;
    width: 1000px;
    height: 960px;
  }
  .label svg { display: block; width: 100%; height: 100%; }
  .pattern-field { fill: url(#limeTone); }
  .cloud {
    fill: var(--cream);
    stroke: var(--pink-line);
    stroke-width: 5;
    stroke-linejoin: round;
  }
  .kanji {
    font-family: "Noto Serif JP", serif;
    font-size: 40px;
    fill: var(--magenta);
  }
  .tagline {
    font-family: "Montserrat", sans-serif;
    font-size: 42px;
    fill: var(--magenta);
  }
  .product-name {
    font-family: "Dela Gothic One", sans-serif;
    font-size: 78px;
    fill: var(--ink);
    stroke: #ffffff;
    stroke-width: 5;
    paint-order: stroke;
  }
  .descriptor {
    font-family: "Montserrat", sans-serif;
    font-size: 28px;
    fill: var(--grey);
    letter-spacing: 0.5px;
  }
</style>
</head>
<body>
<main class="canvas">
  <section class="label">
    <svg viewBox="0 0 651 625" preserveAspectRatio="none" xmlns="http://www.w3.org/2000/svg">
      <defs>
        <linearGradient id="limeTone" x1="0" y1="0" x2="1" y2="1">
          <stop offset="0" stop-color="var(--lime-soft)"/>
          <stop offset="1" stop-color="var(--lime)"/>
        </linearGradient>
      </defs>
      <rect class="pattern-field" x="0" y="0" width="651" height="625" role="img" aria-label="Lime green background with a soft repeating floral lattice pattern"/>
      <path class="cloud" d="M252 124 C300 30 520 20 548 205 C620 215 640 300 605 330 C640 450 520 580 334 548 C300 610 230 600 236 565 C120 580 40 470 66 421 C0 370 40 220 108 210 C90 80 220 70 252 124 Z"/>
      <text class="kanji" x="393" y="135" text-anchor="middle">甘酒</text>
      <text class="tagline" x="326" y="218" text-anchor="middle">Traditional</text>
      <text class="tagline" x="326" y="258" text-anchor="middle">Japanese Drink</text>
      <text class="product-name" x="326" y="370" text-anchor="middle" textLength="446" lengthAdjust="spacingAndGlyphs">AMAZAKE</text>
      <text class="descriptor" x="326" y="425" text-anchor="middle" textLength="446" lengthAdjust="spacing">Made out of Fermented Rice</text>
    </svg>
  </section>
</main>
</body>
</html>
```